Rosalind Vetteray Gymnastics Center Business Card

Develop a business card with my RV logo provided. A classy and unique design using the colors black, white, purple and maybe a splash of gold. Add Address (219 W. Lantern Ridge Road Larkfield, Northmere 44871), email (RosalindVetterayGymnasticsCtr@brellomail.com, website (www.RosalindVetterayGymnasticsCenter.example), phone number (216-555-0148) on the card. Social media if there's room also. t: @VetterayGym, i: @VetterayGym, f: @RosalindVetterayGymnasticsCenter

Target Market(s)

Families, children, gymnastics community and beyond

Industry/Entity Type

Business

Contact Information for Business Card

Add name (Rosalind Vetteray) who is the owner. Add logo, add address details, classy font, uniqueness important, rounded edges on business card. Horizontal business card needed.

Font styles to use
Serif
Sans Serif

Colors
6b449b
ffffff

Requirements
Must have
• Must have logo, owner name and owner on card, must have colors purple, white, black where needed in print, and a splash of gold if appropriate. Keep card classy and clean. Must have address of location, phone number, website of business, email and social media.
Nice to have
• I am open here, but I'd appreciate uniqueness. Must be a lasting image for branding...
Should not have
• No kid-like looks...

```html
<!DOCTYPE html>
<html lang="en">
<head>
<meta charset="utf-8">
<title>Rosalind Vetteray Gymnastics Center – Business Card</title>
<link href="https://fonts.googleapis.com/css2?family=Lato:wght@400;700&display=swap" rel="stylesheet">
<style>
  :root {
    --purple: #652d90;
    --purple-text: #5e2a8a;
    --white: #ffffff;
    --ink: #2b2b2b;
    --grey-line: #9a9a9a;
    --backdrop: #e6d2b3;
  }
  html, body {
    margin: 0;
    padding: 0;
    width: 1200px;
    height: 900px;
    overflow: hidden;
    background: var(--backdrop);
    font-family: "Lato", sans-serif;
  }
  .canvas {
    position: relative;
    width: 1200px;
    height: 900px;
  }
  .card {
    position: absolute;
    top: 306px;
    width: 439px;
    height: 271px;
    border-radius: 12px;
    box-sizing: border-box;
  }
  .card-front {
    left: 149px;
    background: var(--white);
  }
  .card-back {
    left: 609px;
    background: var(--purple);
    color: var(--white);
  }

  /* Front */
  .front-brand {
    position: absolute;
    right: 23px;
    top: 92px;
    width: 150px;
    text-align: center;
  }
  .front-brand .brand-name {
    font-weight: 700;
    font-size: 12px;
    line-height: 12px;
    text-transform: uppercase;
    color: var(--purple-text);
    letter-spacing: 0.2px;
  }
  .front-brand .brand-tagline {
    margin-top: 3px;
    padding-top: 2px;
    border-top: 1px solid var(--grey-line);
    font-size: 9.5px;
    line-height: 11px;
    color: var(--purple-text);
  }
  .owner-name {
    position: absolute;
    left: 19px;
    top: 131px;
    margin: 0;
    font-size: 18px;
    line-height: 20px;
    font-weight: 700;
    font-variant: small-caps;
    letter-spacing: 0.4px;
    color: var(--purple-text);
  }
  .owner-title {
    position: absolute;
    left: 19px;
    top: 151px;
    right: 23px;
    display: flex;
    align-items: center;
    font-size: 12.5px;
    line-height: 14px;
    color: var(--ink);
  }
  .owner-title::after {
    content: "";
    flex: 1;
    height: 1px;
    background: var(--grey-line);
    margin-left: 9px;
  }
  .contact-list {
    position: absolute;
    left: 19px;
    top: 176px;
    margin: 0;
    padding: 0;
    list-style: none;
    font-size: 12.5px;
    line-height: 16px;
    color: var(--ink);
  }
  .contact-list li {
    display: flex;
    align-items: center;
  }
  .contact-list svg {
    width: 10px;
    height: 10px;
    margin-right: 4px;
    fill: var(--purple-text);
  }
  .address {
    position: absolute;
    left: 19px;
    top: 234px;
    margin: 0;
    font-size: 12.5px;
    color: var(--ink);
  }

  /* Back */
  .back-brand {
    position: absolute;
    left: 0;
    right: 0;
    top: 84px;
    text-align: center;
    font-weight: 700;
    font-size: 22px;
    line-height: 27px;
    text-transform: uppercase;
    letter-spacing: 1px;
    color: var(--white);
  }
  .back-rule {
    position: absolute;
    left: 67px;
    right: 67px;
    top: 172px;
    height: 1px;
    background: rgba(255, 255, 255, 0.35);
  }
  .social {
    position: absolute;
    left: 0;
    right: 0;
    top: 194px;
    margin: 0;
    text-align: center;
    font-size: 12.5px;
    line-height: 16px;
  }
</style>
</head>
<body>
<main class="canvas">

  <section class="card card-front" aria-label="Business card front">
    <div class="front-brand">
      <div class="brand-name">Rosalind Vetteray<br>Gymnastics Center</div>
      <div class="brand-tagline">Gymnastics, Camps, Yoga &amp; More</div>
    </div>

    <h1 class="owner-name">Rosalind Vetteray</h1>
    <div class="owner-title">Owner</div>

    <ul class="contact-list">
      <li>
        <svg viewBox="0 0 10 10" aria-hidden="true"><path d="M1 2.5 Q1 1 2.5 1 L3.5 1 4.3 3 3.3 3.8 Q4.2 5.8 6.2 6.7 L7 5.7 9 6.5 9 7.5 Q9 9 7.5 9 Q1 8 1 2.5Z"/></svg>
        216-555-0148
      </li>
      <li>
        <svg viewBox="0 0 10 10" aria-hidden="true"><path d="M0.5 2 H9.5 V8.5 H0.5Z M1.2 2.6 5 5.6 8.8 2.6" stroke="#fff" stroke-width="0.8"/></svg>
        RosalindVetterayGymnasticsCtr@brellomail.com
      </li>
      <li>
        <svg viewBox="0 0 10 10" aria-hidden="true"><circle cx="5" cy="5" r="4.5"/><path d="M0.8 5 H9.2 M5 0.6 Q2.5 5 5 9.4 M5 0.6 Q7.5 5 5 9.4" stroke="#fff" stroke-width="0.6" fill="none"/></svg>
        www.RosalindVetterayGymnasticsCenter.example
      </li>
    </ul>

    <p class="address">219 W. Lantern Ridge Road Larkfield, Northmere 44871</p>
  </section>

  <section class="card card-back" aria-label="Business card back">
    <div class="back-brand">Rosalind Vetteray<br>Gymnastics Center</div>
    <div class="back-rule"></div>
    <p class="social">
      chatterline: @VetterayGym &nbsp;|&nbsp; picturely: @VetterayGym<br>
      friendbook: @RosalindVetterayGymnasticsCenter
    </p>
  </section>

</main>
</body>
</html>
```